Triathlon coaching company website design

A website is needed for a coaching company called StrideMosaic. The company provides coaching services to triathletes and other endurance athletes. This includes 1:1 coaching, individualized training plan development, race preparation, and access to guidance and advice on all aspects of developing and maintaining a healthy lifestyle. The design should appeal to all levels of athletes, but be professional in appearance. The tone of the site should be in keeping with the company tagline: Endurance. Resilience. Achievement.

Target Market(s)

All levels of triathletes - beginners to professionals

Industry/Entity Type

It Company

Coding

Coded - Design and coding required

Number of Pages Required

1 page

Colors

Designer to choose colors to be used in the design.

Requirements
Must have
• Pages that should be included must cover: Introductory (Home), description in detail of what we do, description of the main coach (bio) and others types of expert advisors who can be available, link to contact the company, race reports for coaches and athletes that can be regularly updated, links to other sites of potential interest (e.g. other triathlon sites or my facebook page), twitter feed, sign up for email updates. Ability to add other links and pages in future months (e.g. shared calendar access to book meetings, credit card functionality, testimonials)
Should not have
• Not loud or down market feel - target market will largely be highly educated and reasonably affluent

```html
<!DOCTYPE html>
<html lang="en">
<head>
<meta charset="utf-8">
<title>StrideMosaic – Triathlon Coaching</title>
<link href="https://fonts.googleapis.com/css2?family=Lato:wght@400;700;900&display=swap" rel="stylesheet">
<style>
:root{
  --red:#a31f24;
  --ink:#2a2a2a;
  --muted:#555;
  --band:#efefef;
  --white:#fff;
  --dark-btn:#2b2b2b;
  --footer:#1d1d1d;
  --footer-text:#d6d6d6;
}
*{box-sizing:border-box;margin:0;padding:0}
html,body{width:1200px;height:3209px;overflow:hidden}
body{font-family:'Lato',sans-serif;color:var(--muted);background:var(--white);position:relative}
.btn{position:absolute;background:var(--dark-btn);color:var(--white);font-weight:700;font-size:13px;letter-spacing:.5px;display:flex;align-items:center;justify-content:center;text-transform:uppercase}
.section-title{position:absolute;left:0;width:1200px;text-align:center;color:var(--red);font-weight:700;font-size:24px;letter-spacing:.5px;text-transform:uppercase}

/* header */
.site-header{position:absolute;left:0;top:0;width:1200px;height:107px;background:var(--white)}
.brand{position:absolute;left:75px;top:34px;display:flex;align-items:center;gap:10px;color:var(--red);font-weight:900;font-size:30px}
.brand-dot{width:14px;height:14px;background:var(--red);border-radius:50%}
.main-nav a{position:absolute;top:52px;font-size:13px;font-weight:700;color:var(--ink);text-decoration:none;letter-spacing:.3px}
.main-nav a.active{color:var(--red)}

/* hero */
.hero{position:absolute;left:0;top:107px;width:1200px;height:565px;background:linear-gradient(160deg,#6e7a86 0%,#9b8d86 30%,#59616b 55%,#2f4b63 80%,#5a7d95 100%)}
.hero-name{position:absolute;left:0;top:231px;width:1200px;text-align:center;color:var(--white);font-weight:700;font-size:60px;line-height:72px}
.hero-tagline{position:absolute;left:0;top:290px;width:1200px;text-align:center;color:var(--white);font-weight:700;font-size:44px;line-height:54px}
.hero-arrow{position:absolute;top:270px}

/* welcome */
.welcome p{position:absolute;left:94px;top:766px;width:1012px;text-align:center;font-size:15px;line-height:26.5px}

/* services */
.services{position:absolute;left:0;top:988px;width:1200px;height:642px;background:var(--band)}
.card{position:absolute;width:511px;height:180px;background:var(--white)}
.card svg{position:absolute;left:17px;top:20px}
.card h3{position:absolute;left:110px;top:20px;color:var(--red);font-size:18px;font-weight:700;text-transform:uppercase}
.card p{position:absolute;left:110px;top:50px;width:370px;font-size:14px;line-height:22.5px}
.card .more{position:absolute;left:110px;top:145px;font-size:14px;font-weight:700;color:var(--ink)}

/* about */
.about-photo{position:absolute;left:75px;top:1681px;width:511px;height:355px;background:linear-gradient(135deg,#8e9aa6,#c9a78e 55%,#b43a36 75%,#7d8790)}
.about-title{position:absolute;left:614px;top:1678px;color:var(--red);font-size:23px;font-weight:700;text-transform:uppercase}
.about-text{position:absolute;left:614px;top:1722px;width:515px;font-size:15px;line-height:26.7px}

/* testimonials */
.testimonials{position:absolute;left:0;top:2096px;width:1200px;height:413px;background:var(--band)}
.quote{position:absolute;top:122px;width:300px;text-align:center}
.quote p{font-size:15.5px;line-height:24.6px;height:131px}
.avatar{width:66px;height:66px;margin:0 auto;border:3px solid #ddd;background:linear-gradient(135deg,#b9a293,#6f7b86)}
.quote .who{margin-top:20px;color:var(--red);font-weight:700;font-size:15px}

/* race reports */
.race-title{position:absolute;left:75px;top:2560px;color:var(--red);font-size:24px;font-weight:700;text-transform:uppercase}
.race-text{position:absolute;left:75px;top:2603px;width:515px;font-size:15px;line-height:25.9px}
.results-image{position:absolute;left:614px;top:2565px;width:513px;height:357px;background:linear-gradient(180deg,#f4f4f4 0%,#ececec 45%,#dedede 100%);border:2px solid #ccc}

/* footer */
.site-footer{position:absolute;left:0;top:2984px;width:1200px;height:225px;background:var(--footer);color:var(--footer-text)}
.foot-brand{position:absolute;left:75px;top:52px;color:var(--white);font-weight:900;font-size:26px}
.copyright{position:absolute;left:75px;top:122px;font-size:12px;line-height:26px}
.foot-col{position:absolute;top:44px}
.foot-col h4{color:var(--white);font-size:14px;font-weight:700;text-transform:uppercase;margin-bottom:8px}
.foot-col li{list-style:none;font-size:12.5px;line-height:24px}
.signup{position:absolute;left:868px;top:79px;display:flex}
.signup .field{width:214px;height:38px;background:var(--white);color:#333;font-size:12px;padding:12px 14px}
.signup .go{width:43px;height:38px;background:var(--red);color:var(--white);font-weight:700;font-size:14px;display:flex;align-items:center;justify-content:center}
.social{position:absolute;left:868px;top:142px;display:flex;gap:20px}
.social span{width:14px;height:14px;border-radius:50%;background:var(--white)}
</style>
</head>
<body>

<header class="site-header">
  <div class="brand"><span class="brand-dot"></span>StrideMosaic</div>
  <nav class="main-nav">
    <a class="active" style="left:563px">HOME</a>
    <a style="left:657px">WHAT WE DO</a>
    <a style="left:804px">BIO</a>
    <a style="left:881px">RACE REPORTS</a>
    <a style="left:1035px">CONTACT US</a>
  </nav>
</header>

<section class="hero" role="img" aria-label="Triathletes running, cycling and swimming">
  <div class="hero-name">StrideMosaic</div>
  <div class="hero-tagline">Endurance. Resilience. Achievement.</div>
  <svg class="hero-arrow" style="left:60px" width="16" height="28" viewBox="0 0 16 28"><path d="M14 2 3 14l11 12" fill="none" stroke="#111" stroke-width="4"/></svg>
  <svg class="hero-arrow" style="left:1122px" width="16" height="28" viewBox="0 0 16 28"><path d="M2 2l11 12L2 26" fill="none" stroke="#111" stroke-width="4"/></svg>
</section>

<section class="welcome">
  <h2 class="section-title" style="top:718px">Welcome to our website</h2>
  <p>Aliquam molestie, mi et imperdiet euismod, dui purus auctor tellus, et interdum lacus lectus et ante. Sed accumsan sollicitudin sapien, sit amet adipiscing turpis gravida ac. In congue, neque ac lobortis volutpat, libero mauris varius mi, vitae suscipit ipsum ligula vitae risus. Duis aliquam nibh a dui iaculis viverra id a velit. Vivamus egestas risus in magna varius commodo. Sed semper viverra egestas</p>
  <div class="btn" style="left:511px;top:877px;width:180px;height:47px">Read More</div>
</section>

<section class="services">
  <h2 class="section-title" style="top:35px">What we do</h2>

  <article class="card" style="left:75px;top:99px">
    <svg width="72" height="48" viewBox="0 0 72 48" fill="#333"><circle cx="14" cy="10" r="6"/><path d="M4 40l8-20 14 6-4 4-8-3-4 13z"/><circle cx="50" cy="10" r="6"/><path d="M40 22h18l8 18h-6l-5-10-6 10h-6l5-12z"/></svg>
    <h3>1:1 Coaching</h3>
    <p>Endurance sports require a complex mix of variables to be managed in harmony if goals are to be achieved. Triathlon is particularly complex given the mix of swim, bike, run, nutrition and psychology..</p>
    <span class="more">Read More</span>
  </article>

  <article class="card" style="left:614px;top:99px">
    <svg width="60" height="60" viewBox="0 0 60 60" fill="#333"><rect x="22" y="2" width="34" height="24" fill="none" stroke="#333" stroke-width="3"/><path d="M28 20l8-8 6 5 8-8" fill="none" stroke="#333" stroke-width="2"/><circle cx="12" cy="12" r="5"/><path d="M6 20h12l6 6-2 3-6-4v10H8z"/><circle cx="14" cy="44" r="4"/><circle cx="30" cy="44" r="4"/><circle cx="46" cy="44" r="4"/><path d="M8 58v-6h12v6zm16 0v-6h12v6zm16 0v-6h12v6z"/></svg>
    <h3>Training Plan Development</h3>
    <p>A structured training plan is the most basic requirement of an endurance athlete. This enables a progression of fitness and preparation that is appropriate to the athlete...</p>
    <span class="more">Read More</span>
  </article>

  <article class="card" style="left:75px;top:308px">
    <svg width="60" height="60" viewBox="0 0 60 60" fill="#333"><circle cx="12" cy="14" r="6"/><circle cx="48" cy="14" r="6"/><rect x="30" y="2" width="14" height="10" rx="2"/><path d="M6 24h12v18H6zm36 0h12v18H42zM22 32h16v4h-6v20h-4V36h-6z"/><path d="M6 42h4v14H6zm44 0h4v14h-4z"/></svg>
    <h3>Consultation</h3>
    <p>For those athletes who largely self-manage their training, there is often a benefit from every so often checking with an objective third party on their plan and the progress...</p>
    <span class="more">Read More</span>
  </article>

  <article class="card" style="left:614px;top:308px">
    <svg width="60" height="60" viewBox="0 0 60 60" fill="#333"><circle cx="18" cy="8" r="6"/><circle cx="42" cy="8" r="6"/><path d="M10 18h16v20h-4v20h-8V38h-4zm24 0h16v20h-4v20h-8V38h-4z"/><path d="M26 22l8-6 2 3-8 6z"/></svg>
    <h3>Lifestyle Coaching</h3>
    <p>Triathlon and endurance racing are demanding interests to pursue. For many the interest develops into a passion, and the passion into a lifestyle. Our lives are made up of more than our hobbies and interests...</p>
    <span class="more">Read More</span>
  </article>

  <div class="btn" style="left:511px;top:533px;width:178px;height:47px">View All Services</div>
</section>

<section class="about">
  <div class="about-photo" role="img" aria-label="Smiling coach in cycling helmet holding a road bike over his shoulder"></div>
  <h2 class="about-title">About me Martin Ashcombe</h2>
  <p class="about-text">Triathlon is my passion which, in the past, coexisted with my day job as a management consultant - so I absolutely understand the challenges of fitting triathlon into a busy work, family and social life. I started competing in endurance sports in my teens as a rower, ultimately competing for Great Britain at the World Championships, and have continued as an endurance athlete throughout my life. My first triathlon was an Olympic distance event in Japan in 2001, which sparked my interest in the complexities and rewards of multi-sport and long distance racing.</p>
  <div class="btn" style="left:614px;top:1991px;width:180px;height:47px">Read More</div>
</section>

<section class="testimonials">
  <h2 class="section-title" style="top:46px">Testimonials</h2>
  <div class="quote" style="left:130px">
    <p>“ Aliquam molestie, mi et imperdiet euismod, dui purus auctor tellus, et interdum lacus lectus et ante. Sed accumsan sollicitudin sapien, sit amet adipiscing turpis gravida ac...”</p>
    <div class="avatar" role="img" aria-label="Client portrait"></div>
    <div class="who">-Name Heading</div>
  </div>
  <div class="quote" style="left:449px">
    <p>“ Aliquam molestie, mi et imperdiet euismod, dui purus auctor tellus, et interdum lacus lectus et ante. Sed accumsan sollicitudin sapien, sit amet adipiscing turpis gravida ac...”</p>
    <div class="avatar" role="img" aria-label="Client portrait"></div>
    <div class="who">-Name Heading</div>
  </div>
  <div class="quote" style="left:810px">
    <p>“ Aliquam molestie, mi et imperdiet euismod, dui purus auctor tellus, et interdum lacus lectus et ante. Sed accumsan sollicitudin sapien, sit amet adipiscing turpis gravida ac...”</p>
    <div class="avatar" role="img" aria-label="Client portrait"></div>
    <div class="who">-Name Heading</div>
  </div>
</section>

<section class="race-reports">
  <h2 class="race-title">Race Reports</h2>
  <p class="race-text">Aliquam molestie, mi et imperdiet euismod, dui purus auctor tellus, et interdum lacus lectus et ante. Sed accumsan sollicitudin sapien, sit amet adipiscing turpis gravida ac. In congue, neque ac lobortis volutpat, libero mauris varius mi, vitae suscipit ipsum ligula vitae risus aliquam nibh a dui iaculis viverra id a velit. Vivamus egestas risus in magna varius commodo. Sed semper viverra egestas. Etiam pretium porttitor lectus, vel ornare neque porta volutpat. Suspendisse lobortis turpis in odio blandit ac interdum lorem euismod. Etiam risus massa, vulputate eu pellentesque et, consectetur a neque.</p>
  <div class="btn" style="left:75px;top:2877px;width:180px;height:45px">Read More</div>
  <div class="results-image" role="img" aria-label="Illustrated triathlon race results table with swimmer, cyclist and runner figures"></div>
</section>

<footer class="site-footer">
  <div class="foot-brand">StrideMosaic</div>
  <div class="copyright">Copyright © 2018. Company Name.<br>All Right Reserved</div>

  <div class="foot-col" style="left:359px">
    <h4>Site Map</h4>
    <ul><li>Home</li><li>What we do</li><li>Bio</li><li>Race Reports</li><li>Contact us</li></ul>
  </div>
  <div class="foot-col" style="left:597px">
    <h4>Services</h4>
    <ul><li>1:1 Coaching</li><li>Training Plan Development</li><li>Consultation</li><li>Lifestyle Coaching</li></ul>
  </div>
  <div class="foot-col" style="left:873px">
    <h4>Email Sign Up</h4>
  </div>
  <div class="signup"><div class="field">Enter Email Address</div><div class="go">GO</div></div>
  <div class="social"><span></span><span></span><span></span><span></span><span></span></div>
</footer>

</body>
</html>
```